Velmora Education General Flyer Design

Updates
Reason: We are very close to making a selection but would like to provide a little more time for some of the designers to complete their revisions.
Target Market(s)
Secondary school students
Industry/Entity Type
Education
Requirements
Must have
- company logo and company name (see attached file)

```html
<!DOCTYPE html>
<html lang="en">
<head>
<meta charset="utf-8">
<title>Velmora Education – Math Tutoring Flyer</title>
<link href="https://fonts.googleapis.com/css2?family=Montserrat:wght@400;600;700;800&family=Open+Sans:wght@400;600;700&family=Oswald:wght@600&display=swap" rel="stylesheet">
<style>
  :root {
    --maroon: #8a2a35;
    --badge-red: #c9283a;
    --white: #ffffff;
    --map-tone: #e2e0db;
  }
  * { margin: 0; padding: 0; box-sizing: border-box; }
  html, body { width: 776px; height: 1200px; overflow: hidden; background: var(--white); }
  .flyer {
    position: relative; width: 776px; height: 1200px; overflow: hidden;
    background: var(--white); font-family: "Open Sans", Arial, sans-serif;
  }
  .hero-photo {
    position: absolute; left: 0; top: 0; width: 776px; height: 530px;
    background:
      radial-gradient(ellipse 160px 190px at 520px 150px, #e9b99b 0%, rgba(233,185,155,0) 100%),
      radial-gradient(ellipse 200px 260px at 700px 260px, #8aa866 0%, rgba(138,168,102,0) 100%),
      radial-gradient(ellipse 220px 200px at 330px 330px, #6d6a66 0%, rgba(109,106,102,0) 100%),
      linear-gradient(100deg, #c98a7a 0%, #a86b4f 30%, #7a5643 55%, #b58a68 80%, #9fae78 100%);
  }
  .hero-fade {
    position: absolute; left: 0; top: 480px; width: 776px; height: 50px;
    background: linear-gradient(rgba(255,255,255,0), var(--white));
  }
  .services { position: absolute; left: 55px; top: 52px; color: var(--white); }
  .services h2 {
    font-weight: 700; font-size: 20px; letter-spacing: 0.3px; margin-bottom: 4px;
  }
  .services ul { list-style: none; }
  .services li { position: relative; padding-left: 29px; font-size: 21px; line-height: 32px; }
  .services li::before {
    content: ""; position: absolute; left: 2px; top: 11px; width: 12px; height: 12px;
    background: var(--white);
  }
  .services li.plain::before { display: none; }
  .brand {
    position: absolute; left: 428px; top: 415px; display: flex; align-items: center; gap: 10px;
    color: var(--maroon); font-family: "Montserrat", Arial, sans-serif; font-weight: 800;
    font-size: 26px; line-height: 30px;
  }
  .brand-square { width: 22px; height: 22px; background: var(--maroon); flex: none; }
  .trial-badge { position: absolute; left: 58px; top: 412px; width: 256px; height: 256px; }
  .trial-text {
    position: absolute; left: 58px; top: 460px; width: 256px; text-align: center; color: var(--white);
  }
  .trial-text .title {
    font-family: "Oswald", Arial, sans-serif; font-weight: 600; font-size: 32px; line-height: 32px;
  }
  .trial-text .note { font-weight: 700; font-size: 16.5px; line-height: 20px; margin-top: 2px; }
  .website {
    position: absolute; right: 71px; top: 574px; color: var(--maroon);
    font-family: "Montserrat", Arial, sans-serif; font-weight: 700; font-size: 18px;
  }
  .headline {
    position: absolute; right: 56px; top: 630px; text-align: right; color: var(--maroon);
    font-family: "Montserrat", Arial, sans-serif; font-weight: 800; font-size: 69px;
    line-height: 70px; letter-spacing: 0;
  }
  .tagline {
    position: absolute; right: 56px; top: 838px; text-align: right; color: var(--maroon);
    font-weight: 400; font-size: 33px; line-height: 36px;
  }
  .map-area {
    position: absolute; left: 200px; top: 955px; width: 576px; height: 245px;
    background: var(--map-tone);
    clip-path: polygon(258px 0, 576px 0, 576px 245px, 0 245px);
  }
  .corner-band { position: absolute; left: 0; top: 770px; width: 776px; height: 430px; }
  .contact {
    position: absolute; left: 57px; top: 898px; color: var(--white);
    font-size: 17.5px; line-height: 21px; font-style: normal;
  }
  .contact p { margin-bottom: 16px; }
  .contact strong { font-weight: 700; font-size: 18px; }
</style>
</head>
<body>
<div class="flyer">
  <div class="hero-photo" role="img" aria-label="Photo of smiling secondary school students studying together at a desk"></div>
  <div class="hero-fade"></div>

  <section class="services">
    <h2>MATH WE TUTOR</h2>
    <ul>
      <li>Ontario Math G.9 – 12</li>
      <li>IB Math High Level ,<br>Standard Level, Math Studies</li>
      <li>AP Calculus AB/BC</li>
      <li class="plain">University Year 1<br>Calculus</li>
    </ul>
  </section>

  <div class="brand"><span class="brand-square"></span><span>Velmora<br>Education</span></div>

  <svg class="trial-badge" viewBox="0 0 256 256" aria-hidden="true">
    <polygon fill="var(--white)" points="128,2 146,20 168,8 180,30 205,26 208,51 232,58 224,82 246,96 232,116 250,134 230,148 242,172 218,180 220,205 195,206 186,230 162,222 146,244 128,228 110,244 94,222 70,230 61,206 36,205 38,180 14,172 26,148 6,134 24,116 10,96 32,82 24,58 48,51 51,26 76,30 88,8 110,20"/>
    <polygon fill="var(--badge-red)" points="128,12 145,29 166,18 177,38 200,35 203,58 225,64 218,86 238,99 225,117 241,134 223,147 233,169 211,176 213,199 190,200 182,222 160,214 145,234 128,220 111,234 96,214 74,222 66,200 43,199 45,176 23,169 33,147 15,134 31,117 18,99 38,86 31,64 53,58 56,35 79,38 90,18 111,29"/>
  </svg>
  <div class="trial-text">
    <div class="title">FREE<br>TRIAL LESSON</div>
    <div class="note">Try us out<br>before you enrol!<br>Call or email us today<br>for a Free<br>Trial Lesson.</div>
  </div>

  <div class="website">www.VelmoraEducation.com</div>

  <h1 class="headline">MATH FROM<br>ABSTRACT<br>TO CONCRETE</h1>
  <p class="tagline">We can help make<br>the connection</p>

  <div class="map-area" role="img" aria-label="Street map showing the tutoring centre location"></div>

  <svg class="corner-band" viewBox="0 770 776 430" aria-hidden="true">
    <polygon fill="var(--maroon)" points="0,778 458,960 200,1200 0,1200"/>
  </svg>

  <address class="contact">
    <p>4120 Alder Road,<br>Unit 310, Markham,<br>ON L3R 0A1</p>
    <p><strong>Email</strong><br>Service@VelmoraEducation.com</p>
    <p><strong>Tel</strong><br>647-555-0148</p>
  </address>
</div>
</body>
</html>
```